Create Brisk Lesson Studio a card design that will stick in the mind of prospects.

Brisk Lesson Studio specialises designs and produces training video, animation, illustration and text.

We need a card design that oozes class and leaves the prospect brimming with confidence.

The design will feature the Brisk Lesson Studio all black logo (uploaded). The design may also use the shade of orange from the orange version of the logo (uploaded). Note, just the color is to be used e.g. for the back of the card, not the orange logo itself.

The Brisk brand is about authenticity, quality, maturity and assurance. We are a safe buy when it comes to the prospects next project.

Target Market(s)

The primary target is training managers or others who are responsible for choosing to hire companies to produce their training media e.g. video. This will usually be a large spend so they need to have confidence.

Industry/Entity Type

Training

Contact Information for Business Card

FRONT:

Brisk Lesson Studio
Phone: 03 5172 4039
1st Floor, 418 Kellerby Road
Mt Ferncombe
VIC 3862
Australia
www.brisklesson.com.au

Lionel Petch
Founder and Lead Consultant
mobile: +61 3 0462 735 218
email: lionel@brisklesson.com.au

BACK:
Specialising in design and production of training:

video
animation
illustration
text

for delivery via internet, intranet and/or LMS.

Number of Pages Required

4 page

Font styles to use
Sans Serif

Requirements
Must have
• The black logo uploaded with the brief.
Nice to have
• The inclusion of the shade of orange found in the orange logo also uploaded with the brief. One example would be having the back of the card in this orange and using a white font for the text. But I want the designer to work this out.
Should not have
• No colours other than black and the orange included in the uploaded orange logo.

```html
<!DOCTYPE html>
<html lang="en">
<head>
<meta charset="utf-8">
<title>Brisk Lesson Studio – Business Cards</title>
<link href="https://fonts.googleapis.com/css2?family=Lato:wght@400;700;900&display=swap" rel="stylesheet">
<style>
  :root {
    --backdrop: #d1d2d4;
    --card: #ffffff;
    --ink: #231f20;
    --orange: #f15a22;
    --rule: #8a8a8a;
    --white: #ffffff;
  }
  * { margin: 0; padding: 0; box-sizing: border-box; }
  html, body {
    width: 1200px; height: 2184px; overflow: hidden;
    background: var(--backdrop);
    font-family: "Lato", Arial, sans-serif;
    color: var(--ink);
  }
  .card {
    position: absolute; left: 234px; width: 731px; height: 447px;
    background: var(--card); border-radius: 32px;
    box-shadow: 0 3px 10px rgba(0,0,0,0.18);
  }
  .card--front-a { top: 79px; }
  .card--back-a { top: 604px; }
  .card--front-b { top: 1131px; }
  .card--back-b { top: 1658px; background: var(--orange); color: var(--white); }

  .brand {
    position: absolute; display: flex; align-items: center; gap: 16px;
  }
  .brand__dot {
    width: 40px; height: 40px; border-radius: 50%;
    border: 4px solid currentColor; flex: none;
  }
  .brand__name {
    font-weight: 900; font-size: 46px; line-height: 1.0; letter-spacing: 0.5px;
  }
  .card__brand { left: 42px; top: 100px; }
  .back__brand { left: 0; right: 0; top: 130px; justify-content: center; }
  .back__brand .brand__name { font-size: 58px; }
  .back__brand .brand__dot { width: 52px; height: 52px; border-width: 5px; }

  .person { position: absolute; left: 365px; top: 110px; }
  .person__name { font-weight: 700; font-size: 26px; letter-spacing: 0.5px; text-transform: uppercase; line-height: 1.2; }
  .person__name--accent { color: var(--orange); }
  .person__role { font-size: 17.5px; margin-top: 2px; letter-spacing: 0.3px; }
  .person__contacts { list-style: none; margin-top: 16px; font-size: 17.5px; letter-spacing: 0.3px; }
  .person__contacts li { display: flex; align-items: center; gap: 10px; height: 27px; }
  .person__contacts svg { width: 16px; height: 16px; fill: var(--orange); flex: none; }

  .company { position: absolute; left: 42px; right: 42px; top: 336px; }
  .company__head { display: flex; align-items: center; gap: 10px; }
  .company__name { font-weight: 700; font-size: 17.5px; letter-spacing: 0.4px; text-transform: uppercase; white-space: nowrap; }
  .company__rule { flex: 1; height: 2px; background: var(--rule); }
  .company__details { display: flex; justify-content: space-between; margin-top: 12px; font-size: 17.5px; line-height: 26px; letter-spacing: 0.3px; }
  .company__address { text-align: right; margin-top: -4px; }

  .tagline { position: absolute; left: 46px; right: 42px; top: 364px; }
  .tagline__lead { display: flex; align-items: center; gap: 12px; font-size: 17.5px; letter-spacing: 0.3px; white-space: nowrap; }
  .tagline__rule { flex: 1; height: 2px; background: var(--rule); }
  .card--back-b .tagline__rule { background: var(--white); }
  .card--back-b .tagline__lead { font-weight: 700; }
  .services { list-style: none; display: flex; justify-content: center; align-items: center; margin-top: 12px; font-weight: 700; font-size: 18.5px; letter-spacing: 1.4px; text-transform: uppercase; }
  .services li + li::before { content: "•"; margin: 0 20px; }
</style>
</head>
<body>

<!-- Front, black name -->
<section class="card card--front-a">
  <div class="brand card__brand"><span class="brand__dot"></span><span class="brand__name">Brisk<br>Lesson<br>Studio</span></div>
  <div class="person">
    <h2 class="person__name">Lionel Petch</h2>
    <p class="person__role">Founder / Lead Consultant</p>
    <ul class="person__contacts">
      <li><svg viewBox="0 0 16 16"><path d="M4 0h8a1 1 0 0 1 1 1v14a1 1 0 0 1-1 1H4a1 1 0 0 1-1-1V1a1 1 0 0 1 1-1zm1 2v10h6V2zm3 11a1 1 0 1 0 0 2 1 1 0 0 0 0-2z"/></svg>+61 3 0462 735 218</li>
      <li><svg viewBox="0 0 16 16"><path d="M0 3h16v1.2L8 9 0 4.2zM0 6l8 4.8L16 6v7H0z"/></svg>lionel@brisklesson.com.au</li>
    </ul>
  </div>
  <div class="company">
    <div class="company__head"><span class="company__name">Brisk Lesson Studio</span><span class="company__rule"></span></div>
    <div class="company__details">
      <p>P: 03 5172 4039<br>www.brisklesson.com.au</p>
      <p class="company__address">1st Floor, 418 Kellerby Road<br>Mt Ferncombe, VIC 3862 Australia</p>
    </div>
  </div>
</section>

<!-- Back, white -->
<section class="card card--back-a">
  <div class="brand back__brand"><span class="brand__dot"></span><span class="brand__name">Brisk Lesson<br>Studio</span></div>
  <div class="tagline">
    <p class="tagline__lead"><span class="tagline__rule"></span>Specialising in design and production of training<span class="tagline__rule"></span></p>
    <ul class="services"><li>Video</li><li>Animation</li><li>Illustration</li><li>Text</li></ul>
  </div>
</section>

<!-- Front, orange name -->
<section class="card card--front-b">
  <div class="brand card__brand"><span class="brand__dot"></span><span class="brand__name">Brisk<br>Lesson<br>Studio</span></div>
  <div class="person">
    <h2 class="person__name person__name--accent">Lionel Petch</h2>
    <p class="person__role">Founder / Lead Consultant</p>
    <ul class="person__contacts">
      <li><svg viewBox="0 0 16 16"><path d="M4 0h8a1 1 0 0 1 1 1v14a1 1 0 0 1-1 1H4a1 1 0 0 1-1-1V1a1 1 0 0 1 1-1zm1 2v10h6V2zm3 11a1 1 0 1 0 0 2 1 1 0 0 0 0-2z"/></svg>+61 3 0462 735 218</li>
      <li><svg viewBox="0 0 16 16"><path d="M0 3h16v1.2L8 9 0 4.2zM0 6l8 4.8L16 6v7H0z"/></svg>lionel@brisklesson.com.au</li>
    </ul>
  </div>
  <div class="company">
    <div class="company__head"><span class="company__name">Brisk Lesson Studio</span><span class="company__rule"></span></div>
    <div class="company__details">
      <p>P: 03 5172 4039<br>www.brisklesson.com.au</p>
      <p class="company__address">1st Floor, 418 Kellerby Road<br>Mt Ferncombe, VIC 3862 Australia</p>
    </div>
  </div>
</section>

<!-- Back, orange -->
<section class="card card--back-b">
  <div class="brand back__brand"><span class="brand__dot"></span><span class="brand__name">Brisk Lesson<br>Studio</span></div>
  <div class="tagline">
    <p class="tagline__lead"><span class="tagline__rule"></span>Specialising in design and production of training<span class="tagline__rule"></span></p>
    <ul class="services"><li>Video</li><li>Animation</li><li>Illustration</li><li>Text</li></ul>
  </div>
</section>

</body>
</html>
```